Homemaking training schools needs a Business Card design

Designer, Hello!

No special requirements, good-looking enough.
--------------------------------------------------------------------------

Name: Marcus Liao
Chairman
Tel: 0574-57418263
Mobile: 13852247106
Email: kelvory@mailpond.com
Web: www.tqb2031.com
Add: No.258, LinfengJie, DaoyueQu, Ningbo, Zhejiang

LOGO
Ningbo TQB Homemaking Training School

Target Market(s)

pregnant women, mothers, infants, the elderly and families, including cleaning, cooking, nursing training.

Industry/Entity Type

Business

Contact Information for Business Card

Name: Marcus Liao
Chairman
Tel: 0574-57418263
Mobile: 13852247106
Email: kelvory@mailpond.com
Web: www.tqb2031.com

LOGO

Font styles to use
Serif
Sans Serif
Decorative

Requirements
Nice to have
• Feels: clean, specifications, safety, comfort, warmth and happiness.

```html
<!DOCTYPE html>
<html lang="en">
<head>
<meta charset="utf-8">
<title>TaoQianBo Training &amp; Services – Business Card</title>
<link rel="stylesheet" href="https://fonts.googleapis.com/css2?family=Questrial&display=swap">
<style>
  :root {
    --page-bg: #e6e7ea;
    --card-white: #ffffff;
    --card-grey: #e9eaec;
    --brand-blue: #1f6db3;
    --brand-blue-dark: #175b98;
    --brand-pink: #e0248a;
    --rule-grey: #5d6168;
    --text-light: #ffffff;
  }
  * { box-sizing: border-box; margin: 0; padding: 0; }
  html, body {
    width: 1200px; height: 997px; overflow: hidden;
    background: var(--page-bg);
    font-family: "Questrial", "Century Gothic", sans-serif;
  }
  .sheet {
    position: relative; width: 1200px; height: 997px;
    display: flex; flex-direction: column; align-items: center; justify-content: center; gap: 60px;
  }
  .card {
    position: relative; width: 700px; height: 400px;
    border-radius: 18px; overflow: hidden;
    background: linear-gradient(160deg, var(--card-white) 40%, var(--card-grey));
    box-shadow: 0 6px 18px rgba(0,0,0,.18);
  }

  /* brand lockup */
  .brand { position: absolute; text-align: center; }
  .brand-row { display: flex; align-items: center; gap: 12px; justify-content: center; }
  .brand-dot { width: 22px; height: 22px; border-radius: 50%; background: var(--brand-pink); }
  .brand-name { color: var(--brand-blue); font-size: 58px; letter-spacing: 1px; line-height: 1; }
  .brand-tagline {
    display: flex; align-items: center; gap: 10px; margin-top: 8px;
    color: var(--rule-grey); font-size: 19px; letter-spacing: 1px;
  }
  .brand-tagline::before, .brand-tagline::after {
    content: ""; flex: 1; height: 1.5px; background: var(--rule-grey);
  }

  /* front */
  .card-front .brand { left: 0; right: 0; top: 110px; margin: 0 auto; width: 460px; }
  .front-band {
    position: absolute; left: 0; right: 0; bottom: 0; height: 92px;
    background: var(--brand-blue); border-top: 6px solid var(--brand-pink);
    display: flex; align-items: center; justify-content: center;
  }
  .front-band .notch {
    position: absolute; top: -6px; left: 50%; transform: translateX(-50%);
    width: 0; height: 0;
    border-left: 12px solid transparent; border-right: 12px solid transparent;
    border-top: 12px solid var(--brand-pink);
  }
  .web { color: var(--text-light); font-size: 24px; letter-spacing: 3px; }

  /* back */
  .card-back .brand { left: 40px; top: 150px; width: 320px; }
  .card-back .brand-name { font-size: 44px; }
  .card-back .brand-tagline { font-size: 16px; }
  .info-panel {
    position: absolute; top: 0; right: 0; bottom: 0; width: 300px;
    background: var(--brand-blue); border-left: 6px solid var(--brand-pink);
    color: var(--text-light); padding: 42px 24px 0 36px;
  }
  .info-panel .notch {
    position: absolute; left: 0; top: 50px;
    width: 0; height: 0;
    border-top: 10px solid transparent; border-bottom: 10px solid transparent;
    border-left: 12px solid var(--brand-pink);
  }
  .person-name { font-size: 26px; }
  .person-title { font-size: 15px; margin-top: 2px; }
  .contact-list { list-style: none; margin-top: 70px; display: flex; flex-direction: column; gap: 16px; }
  .contact-item { display: flex; align-items: flex-start; gap: 14px; font-size: 16px; letter-spacing: .5px; line-height: 1.2; }
  .contact-icon {
    flex: none; width: 22px; height: 20px; border-radius: 3px;
    background: #f2f2f4; display: flex; align-items: center; justify-content: center;
  }
  .contact-icon svg { width: 14px; height: 14px; fill: var(--brand-pink); }
</style>
</head>
<body>
<main class="sheet">

  <section class="card card-front" aria-label="Card front">
    <div class="brand">
      <div class="brand-row"><span class="brand-dot"></span><span class="brand-name">TaoQianBo</span></div>
      <div class="brand-tagline">Training &amp; Services</div>
    </div>
    <div class="front-band">
      <span class="notch"></span>
      <span class="web">www.tqb2031.com</span>
    </div>
  </section>

  <section class="card card-back" aria-label="Card back">
    <div class="brand">
      <div class="brand-row"><span class="brand-dot"></span><span class="brand-name">TaoQianBo</span></div>
      <div class="brand-tagline">Training &amp; Services</div>
    </div>
    <div class="info-panel">
      <span class="notch"></span>
      <p class="person-name">Marcus Liao</p>
      <p class="person-title">Chairman</p>
      <ul class="contact-list">
        <li class="contact-item">
          <span class="contact-icon"><svg viewBox="0 0 16 16"><path d="M1 6c0-2 3-4 7-4s7 2 7 4v1h-4V5.5H5V7H1z M3 8h10l1 6H2z"/></svg></span>
          <span>0574-57418263</span>
        </li>
        <li class="contact-item">
          <span class="contact-icon"><svg viewBox="0 0 16 16"><rect x="4" y="1" width="8" height="14" rx="1.5"/></svg></span>
          <span>13852247106</span>
        </li>
        <li class="contact-item">
          <span class="contact-icon"><svg viewBox="0 0 16 16"><path d="M1 3h14v10H1z M1 3l7 6 7-6" stroke="#f2f2f4" stroke-width="1"/></svg></span>
          <span>kelvory@mailpond.com</span>
        </li>
        <li class="contact-item">
          <span class="contact-icon"><svg viewBox="0 0 16 16"><path d="M8 1L1 8h2v7h4v-4h2v4h4V8h2z"/></svg></span>
          <span>No.258, LinfengJie, DaoyueQu<br>Ningbo, Zhejiang</span>
        </li>
      </ul>
    </div>
  </section>

</main>
</body>
</html>
```